Health and Wellness Company Business Card

I need a business card design that is clean and uses modern minimalist style. The design should incorporate our logo (see attached). I would also like to use embossing on the cards so that they also have a great feel. I am open to the card using one or more colors, and these do not have to correspond to the colors in the concept paper. The card can either be one-sided or use both sides of the card.The logo uses the Avenir font.

I will need the file designed in Adobe CS and compatible with CS5.5 (Illustrator preferable) and I'll need the working file (for example: .ai) once the project is complete so that I can change the names/contact info/etc for each variation of the card.

This needs to be a memorable card for the recipient. They should think: "This is a great business card" either because of its simplicity or embossing effects or use of color.

Target Market(s)

The audience for our company has two main groups: people who pay for healthcare (insurers, companies, researcher companies) and people with chronic health conditions who are the consumers of our services and resources.

Industry/Entity Type

Business

Requirements
Must have
• Essential components of the card include: Company logo, contact Name (Mark Dalton), phone number (5049381726), email address (mdalton@brevolin.com), slogan/tagline that consists of ~30-40 characters (Use Lorem Ipsum)
Nice to have
• These fall just slightly short of "must have" to allow for design flexibility: Embossing or spot varnish effects and a splash of color
Should not have
• Designs with these components will not be successful: flashy or showy designs that are not professional in appearance, and lots of different colors

```html
<!DOCTYPE html>
<html lang="en">
<head>
<meta charset="utf-8">
<title>Brevolin Business Card</title>
<link rel="stylesheet" href="https://fonts.googleapis.com/css2?family=Mulish:wght@400;600&display=swap">
<style>
  :root {
    --backdrop: #2b2b2e;
    --card: #121213;
    --card-edge: #1d1d1f;
    --brand: #9c9cbc;
    --tagline: #55555f;
    --emboss: #0b0b0c;
    --emboss-light: rgba(255,255,255,0.12);
  }
  * { margin: 0; padding: 0; box-sizing: border-box; }
  html, body {
    width: 1200px;
    height: 850px;
    overflow: hidden;
    background: var(--backdrop);
    font-family: "Mulish", sans-serif;
  }
  .sheet {
    width: 1200px;
    height: 850px;
    display: flex;
    align-items: center;
    justify-content: center;
    gap: 60px;
  }
  .card {
    position: relative;
    width: 540px;
    height: 309px;
    background: var(--card);
    border: 1px solid var(--card-edge);
    border-radius: 4px;
    box-shadow: 0 18px 40px rgba(0,0,0,0.45);
    overflow: hidden;
  }
  .brand {
    position: absolute;
    display: flex;
    align-items: center;
    gap: 16px;
    color: var(--brand);
    font-weight: 400;
    text-transform: uppercase;
  }
  .brand-dot {
    width: 22px;
    height: 22px;
    border-radius: 50%;
    background: var(--brand);
  }
  .card-front .brand {
    left: 50%;
    top: 50%;
    transform: translate(-50%, -50%);
    font-size: 40px;
    letter-spacing: 0.32em;
  }
  .card-back .brand {
    left: 44px;
    top: 60px;
    font-size: 28px;
    letter-spacing: 0.3em;
  }
  .card-back .brand-dot { width: 16px; height: 16px; }
  .tagline {
    position: absolute;
    left: 44px;
    top: 112px;
    width: 300px;
    color: var(--tagline);
    font-size: 9.5px;
    font-weight: 600;
    line-height: 1.35;
  }
  .contact {
    position: absolute;
    right: 40px;
    bottom: 40px;
    text-align: right;
    color: var(--emboss);
    text-shadow: -1px -1px 0 var(--emboss-light);
  }
  .contact-name { font-size: 24px; font-weight: 600; letter-spacing: 0.02em; }
  .contact-phone { font-size: 24px; font-weight: 600; letter-spacing: 0.04em; }
  .contact-email { font-size: 13px; font-weight: 600; margin-top: 2px; }
</style>
</head>
<body>
  <main class="sheet">
    <section class="card card-front" aria-label="Card front">
      <div class="brand"><span class="brand-dot"></span><span class="brand-name">Brevolin</span></div>
    </section>

    <section class="card card-back" aria-label="Card back">
      <div class="brand"><span class="brand-dot"></span><span class="brand-name">Brevolin</span></div>
      <p class="tagline">
        Lorem Ipsum Lorem Ipsum Lorem Ipsum Lorem Ipsum Lorem Ipsum Lorem Ipsum Lorem Ipsum Lorem Ipsum Lorem Ipsum Lorem Ipsum Lorem Ipsum Lorem Ipsum Lorem Ipsum Lorem Ipsum Lorem Ipsum Lorem Ipsum
      </p>
      <div class="contact">
        <p class="contact-name">Mark Dalton</p>
        <p class="contact-phone">5049381726</p>
        <p class="contact-email">mdalton@brevolin.com</p>
      </div>
    </section>
  </main>
</body>
</html>
```